Profile and Wizard Based Website

The scope of this project is to create a website that will allow users to signup through a wizard. The wizard is already made and will be provided.

Users should also be able to login using their pallnook account and then the wizard will start.

After the the wizard is complete and all the information is captured, the user will have a dashboard that will display different information in different sections of dashboard.

The website will also have different levels of access; user, moderator and admin.

The admin will have the ability to see data reports based on the user information captured from the website.

Deliverables:

- Layouts for login page
- Layouts for the wizard questions (about 10 questions in the wizard, each page will display one question)
- Layouts for Dashboard/Profile login
- Layouts for content and document library (Documents, Videos etc)

More info to come.

Attached is the sample wizard question layout and flow chart for wizard.

```html
<!DOCTYPE html>
<html lang="en">
<head>
<meta charset="UTF-8">
<title>Security Wizard – Smartphone Question</title>
<link href="https://fonts.googleapis.com/css2?family=Montserrat:wght@400;500&display=swap" rel="stylesheet">
<style>
  :root {
    --backdrop: #434343;
    --panel: #ffffff;
    --heading-blue: #1b69be;
    --button-blue: #1769bd;
    --text-dark: #2b2b2b;
    --radio-on: #1fbf98;
    --radio-off: #d9dde3;
    --photo-skin: #e9d2c4;
    --photo-shirt: #b9b7bd;
    --device-dark: #2c3a4f;
    --device-screen: #7fb4d8;
  }
  * { margin: 0; padding: 0; box-sizing: border-box; }
  html, body {
    width: 1200px;
    height: 720px;
    overflow: hidden;
    background: var(--backdrop);
    font-family: "Montserrat", Arial, sans-serif;
  }
  .wizard-panel {
    position: absolute;
    left: 65px;
    top: 35px;
    width: 1089px;
    height: 624px;
    background: var(--panel);
    border-radius: 2px;
  }
  .wizard-heading {
    position: absolute;
    left: 108px;
    top: 60px;
    font-size: 28px;
    font-weight: 500;
    color: var(--heading-blue);
    letter-spacing: 0.2px;
  }
  .agent-photo {
    position: absolute;
    left: 42px;
    top: 132px;
    width: 307px;
    height: 492px;
    background: linear-gradient(180deg, var(--photo-skin) 0%, var(--photo-shirt) 45%, #9d9ca3 80%, #2a2e3a 100%);
    border-radius: 120px 120px 0 0;
  }
  .question {
    position: absolute;
    left: 351px;
    top: 160px;
  }
  .question-title {
    font-size: 21px;
    font-weight: 500;
    color: var(--text-dark);
    margin-bottom: 30px;
  }
  .answer-option {
    display: flex;
    align-items: center;
    gap: 16px;
    margin-left: 30px;
    height: 34px;
    margin-bottom: 29px;
    font-size: 20px;
    font-weight: 500;
    color: var(--text-dark);
  }
  .radio-mark { width: 28px; height: 28px; flex: none; }
  .accept-button {
    position: absolute;
    left: 410px;
    top: 401px;
    width: 176px;
    height: 66px;
    border: none;
    border-radius: 2px;
    background: var(--button-blue);
    color: #fff;
    font-family: "Montserrat", Arial, sans-serif;
    font-size: 24px;
    font-weight: 500;
  }
  .device-photo {
    position: absolute;
    left: 726px;
    top: 291px;
    width: 293px;
    height: 218px;
    background: linear-gradient(160deg, var(--device-screen) 0%, #5f8fb3 45%, var(--device-dark) 100%);
    border-radius: 36px;
    transform: skewY(-18deg) scale(0.9);
  }
</style>
</head>
<body>
  <main class="wizard-panel">
    <h1 class="wizard-heading">Ok, you’re looking for a new security systems.</h1>

    <div class="agent-photo" role="img" aria-label="Photo of a smiling support agent wearing a headset"></div>

    <form class="question">
      <p class="question-title">Do you have a smartphone?</p>
      <label class="answer-option">
        <svg class="radio-mark" viewBox="0 0 28 28" aria-hidden="true">
          <circle cx="14" cy="14" r="11" fill="none" stroke="var(--radio-on)" stroke-width="6"/>
          <circle cx="14" cy="14" r="4" fill="#fff"/>
        </svg>
        Yes, I have a smartphone
      </label>
      <label class="answer-option">
        <svg class="radio-mark" viewBox="0 0 28 28" aria-hidden="true">
          <circle cx="14" cy="14" r="12" fill="none" stroke="var(--radio-off)" stroke-width="3"/>
        </svg>
        No I don’t have a smart hone
      </label>
    </form>

    <button class="accept-button" type="button">Accept</button>

    <div class="device-photo" role="img" aria-label="Photo of a smartphone lying at an angle"></div>
  </main>
</body>
</html>
```